Website for The Tavery Parlour

I require a website for "The Tavery Parlour" which is a blog type business for 40+ year old women covering books, true crime, history, travel and food. It needs to support blog posts, links to social media including YouTube videos, Instagram, TikTok and Facebook. The background theme needs to be like that of a newspaper. Easy to navigate and to allow me to post blogs/videos.

```html
<!DOCTYPE html>
<html lang="en">
<head>
<meta charset="utf-8">
<title>The Tavery Parlour</title>
<link href="https://fonts.googleapis.com/css2?family=Cinzel:wght@600;700;800&family=Arimo:wght@400;700&display=swap" rel="stylesheet">
<style>
:root{
  --cream:#faf6ef;
  --ink:#161616;
  --teal:#163f55;
  --teal-mid:#4f6e82;
  --orange:#f7a21b;
  --pink:#f3b6c1;
  --grey-blue:#9fb2c2;
  --footer:#1d1517;
  --white:#ffffff;
  --body:#2a2a2a;
}
*{margin:0;padding:0;box-sizing:border-box}
html,body{width:1200px;height:4640px;overflow:hidden}
body{position:relative;background:var(--white);font-family:"Arimo",Arial,sans-serif;color:var(--body)}
.abs{position:absolute}
.serif{font-family:"Cinzel",Georgia,serif}

/* hero */
.hero{left:0;top:0;width:1200px;height:800px}
.logo-box{left:536px;top:9px;width:499px;height:99px;background:var(--white);display:flex;align-items:center;justify-content:center}
.wordmark{font-family:"Cinzel",Georgia,serif;font-weight:700;font-size:44px;color:var(--ink);letter-spacing:1px}
.social{top:158px;width:44px;height:44px;border-radius:50%;background:var(--white);border:3px solid var(--teal-mid)}
.nav a{position:absolute;top:230px;color:var(--white);font-weight:700;font-size:27px;text-decoration:none;letter-spacing:.5px}
.nav .contact{left:963px;top:212px;width:166px;height:62px;background:var(--orange);display:flex;align-items:center;justify-content:center}
.headline{right:125px;text-align:right;color:var(--white);font-weight:700;line-height:1}
.h-age{top:302px;right:70px;font-size:84px;letter-spacing:-1px}
.h-topic{font-size:66px;letter-spacing:-.5px}
.h-small{font-size:40px}
.h-vertical{left:1072px;top:400px;width:60px;height:262px;display:flex;align-items:center;justify-content:center}
.h-vertical span{transform:rotate(90deg);white-space:nowrap;color:var(--white);font-weight:700;font-size:60px;letter-spacing:1px}

/* story */
.story-title{top:870px;left:0;width:1200px;text-align:center;color:var(--teal);font-size:80px;font-weight:700}
.story-text{left:124px;top:1012px;width:970px;font-size:22px;line-height:33px;color:var(--ink)}
.pill{width:207px;height:603px;border-radius:104px;overflow:hidden}
.topic{width:205px;text-align:center}
.topic h3{color:var(--teal);font-size:27px;line-height:32px;font-weight:700;margin-bottom:16px}
.topic p{font-size:14.5px;line-height:22.5px;text-align:left;color:var(--ink)}

/* blogs */
.blogs{left:0;top:2349px;width:1200px;height:617px;background:var(--teal)}
.blogs-label{left:30px;top:2448px;width:84px;height:414px;display:flex;align-items:center;justify-content:center}
.blogs-label span{transform:rotate(-90deg);white-space:nowrap;color:var(--white);font-size:74px;font-weight:700;font-family:"Cinzel",Georgia,serif}
.blog-card{width:486px;height:528px;background:var(--cream)}
.blog-card .photo{width:100%;height:306px}
.blog-card p{margin:20px 30px 0 36px;font-size:14.5px;line-height:20.5px;color:var(--ink)}
.read-more{display:inline-block;margin:8px 0 0 36px;background:var(--teal);color:#c7d6de;font-size:23px;padding:3px 10px;border:2px solid var(--cream);outline:1px solid var(--teal)}

/* testimonials */
.testimonials{left:0;top:2997px;width:1200px;height:590px}
.t-title{left:0;top:3030px;width:1200px;text-align:center;font-size:60px;font-weight:800;color:var(--ink)}
.t-card{top:3118px;width:512px;height:405px;background:var(--cream);text-align:center}
.avatar{position:absolute;left:203px;top:9px;width:108px;height:108px;border-radius:50%;border:4px solid var(--white)}
.quote{position:absolute;left:44px;top:30px;font-family:Georgia,serif;font-size:170px;line-height:1;color:#cfcfcf}
.t-card h4{position:absolute;top:125px;left:0;width:100%;color:var(--teal);font-size:28px;font-weight:700}
.t-card p{position:absolute;top:168px;left:28px;width:456px;font-size:14.5px;line-height:23.5px;color:var(--teal)}
.stars{position:absolute;top:350px;left:0;width:100%;display:flex;justify-content:center;gap:10px}

/* thanks */
.thanks{left:0;top:3618px;width:1200px;height:787px;background:linear-gradient(180deg,#f5c1ca,var(--pink))}
.thanks-title{left:640px;top:3890px;width:540px;text-align:center;font-size:50px;font-weight:700;color:#3b2a2a}
.thanks-sub{left:640px;top:3972px;width:540px;text-align:center;font-size:23px;line-height:33px;color:var(--ink)}
.follow{left:750px;top:4073px;width:326px;height:85px;background:var(--teal);color:var(--white);font-weight:700;font-size:28px;line-height:31px;text-align:center;display:flex;align-items:center;justify-content:center;border:2px solid var(--white);outline:1px solid var(--teal)}
.news-label{left:640px;top:4258px;width:545px;text-align:center;color:var(--white);font-weight:700;font-size:24px}
.email{left:626px;top:4300px;width:342px;height:43px;background:var(--white);font-size:13px;padding:14px 0 0 22px;color:var(--ink)}
.signup{left:968px;top:4300px;width:192px;height:43px;background:var(--grey-blue);color:var(--white);font-weight:700;font-size:24px;display:flex;align-items:center;justify-content:center}

/* footer */
.footer{left:0;top:4405px;width:1200px;height:235px;background:var(--footer)}
.f-word{left:45px;top:4468px;font-family:"Cinzel",Georgia,serif;font-weight:700;font-size:34px;color:var(--white)}
.f-icon{top:4537px;width:36px;height:36px;border-radius:50%;border:2px solid var(--white)}
.f-col{color:var(--white)}
.f-col h5{font-size:18px;font-weight:700;margin-bottom:6px;color:var(--white)}
.f-col li{list-style:none;font-size:18.5px;line-height:25px;color:var(--white)}
.f-col p{font-size:14px;line-height:20px;color:var(--white)}
.call{display:inline-block;margin-top:8px;background:var(--orange);color:var(--white);font-weight:700;font-size:17px;padding:5px 18px}
.copy{left:0;top:4602px;width:1200px;text-align:center;font-size:18px;color:var(--white)}
</style>
</head>
<body>

<svg width="0" height="0" style="position:absolute">
  <defs>
    <symbol id="star" viewBox="0 0 24 24"><polygon points="12,1 15,9 23,9 16.5,14 19,22.5 12,17.5 5,22.5 7.5,14 1,9 9,9" fill="#f7a21b"/></symbol>
  </defs>
</svg>

<!-- hero -->
<svg class="abs hero" viewBox="0 0 1200 800" width="1200" height="800">
  <defs>
    <linearGradient id="mapTone" x1="0" y1="0" x2="1" y2="1">
      <stop offset="0" stop-color="#6b8798" stop-opacity="0"/>
      <stop offset="1" stop-color="#3e5f73" stop-opacity=".55"/>
    </linearGradient>
    <linearGradient id="woman" x1="0" y1="0" x2="0" y2="1">
      <stop offset="0" stop-color="#8a6a5a"/>
      <stop offset=".35" stop-color="#e3b084"/>
      <stop offset=".4" stop-color="#f3a81c"/>
      <stop offset="1" stop-color="#e39312"/>
    </linearGradient>
  </defs>
  <rect width="1200" height="800" fill="#ffffff"/>
  <path d="M0,0 H1200 V110 H0 Z" fill="#faf6ef"/>
  <path d="M0,100 C250,50 450,150 700,140 C900,132 1000,80 1200,100 V738 H0 Z" fill="#587789"/>
  <rect x="0" y="100" width="1200" height="638" fill="url(#mapTone)" role="img" aria-label="Vintage map and postage stamps backdrop"/>
  <path d="M0,0 H500 C540,120 560,250 545,420 C560,560 600,700 520,740 C420,790 220,800 0,792 Z" fill="url(#woman)" role="img" aria-label="Smiling woman in a yellow sweater with arms crossed"/>
</svg>
<div class="abs logo-box"><span class="wordmark">The Tavery Parlour</span></div>
<div class="abs social" style="left:968px" role="img" aria-label="Social link one"></div>
<div class="abs social" style="left:1024px" role="img" aria-label="Social link two"></div>
<div class="abs social" style="left:1080px" role="img" aria-label="Social link three"></div>
<nav class="nav">
  <a style="left:478px">HOME</a>
  <a style="left:621px">OUR STORY</a>
  <a style="left:828px">BLOGS</a>
  <a class="contact">CONTACT</a>
</nav>
<div class="abs headline h-age">40+ year old</div>
<div class="abs headline h-topic" style="top:398px">WOMEN</div>
<div class="abs headline h-topic" style="top:454px">COVERING</div>
<div class="abs headline h-topic" style="top:511px">BOOKS</div>
<div class="abs headline h-topic" style="top:568px">TRUE CRIME</div>
<div class="abs headline h-small" style="top:624px">TRAVEL AND FOOD</div>
<div class="abs h-vertical"><span>HISTORY</span></div>

<!-- our story -->
<h1 class="abs serif story-title">OUR STORY</h1>
<p class="abs story-text">Lorem ipsum dolor sit amet, consectetur adipiscing elit, sed do eiusmod tempor incididunt ut labore et dolore magna aliqua. Ut enim ad minim veniam, quis nostrud exercitation ullamco laboris nisi ut aliquip ex ea commodo consequat Duis aute irure dolor in reprehenderit in voluptate velit esse cillum dolore eu fugiat nulla pariatur. Excepteur, sint occaecat cupidatat non proident, sunt in culpa qui officia deserunt mollit anim id es laborum.</p>

<div class="abs pill" style="left:45px;top:1300px;background:linear-gradient(180deg,#c9ccd0,#6b5a3e 50%,#3a3226)" role="img" aria-label="Traveller in a plaid coat with a suitcase"></div>
<div class="abs pill" style="left:270px;top:1440px;background:linear-gradient(180deg,#e9a48a,#f4f1ec 40%,#efe6dc)" role="img" aria-label="Hand colouring a floral drawing"></div>
<div class="abs pill" style="left:495px;top:1291px;background:linear-gradient(180deg,#f8b43a,#d9262e 55%,#c41e2a)" role="img" aria-label="Woman in a red dress holding a cake"></div>
<div class="abs pill" style="left:722px;top:1445px;background:linear-gradient(180deg,#7f9fc4,#cfd6df 45%,#7d8a86)" role="img" aria-label="Historic equestrian statue on a column"></div>
<div class="abs pill" style="left:949px;top:1292px;background:linear-gradient(180deg,#1e2430,#3b3a35 60%,#6d6753)" role="img" aria-label="Night crime scene with chalk outline"></div>

<div class="abs topic" style="left:46px;top:2074px"><h3>Lorem ipsum dolor sit amet</h3><p>Lorem ipsum dolor sit amet, consectetur adipiscing elit, sed do eiusmod tempor incididunt ut labore et dolore magna aliqua.</p></div>
<div class="abs topic" style="left:277px;top:2074px"><h3>Lorem ipsum dolor sit amet</h3><p>Lorem ipsum dolor sit amet, consectetur adipiscing elit, sed do eiusmod tempor incididunt ut labore et dolore magna aliqua.</p></div>
<div class="abs topic" style="left:500px;top:2074px"><h3>Lorem ipsum dolor sit amet</h3><p>Lorem ipsum dolor sit amet, consectetur adipiscing elit, sed do eiusmod tempor incididunt ut labore et dolore magna aliqua.</p></div>
<div class="abs topic" style="left:731px;top:2074px"><h3>Lorem ipsum dolor sit amet</h3><p>Lorem ipsum dolor sit amet, consectetur adipiscing elit, sed do eiusmod tempor incididunt ut labore et dolore magna aliqua.</p></div>
<div class="abs topic" style="left:952px;top:2074px"><h3>Lorem ipsum dolor sit amet</h3><p>Lorem ipsum dolor sit amet, consectetur adipiscing elit, sed do eiusmod tempor incididunt ut labore et dolore magna aliqua.</p></div>

<!-- blogs -->
<section class="abs blogs"></section>
<div class="abs blogs-label"><span>OUR BLOGS</span></div>
<article class="abs blog-card" style="left:148px;top:2394px">
  <div class="photo" style="background:linear-gradient(135deg,#e8ddd6,#c9b3a9 50%,#a7212a)" role="img" aria-label="Dramatic true-crime portrait with red roses"></div>
  <p>Lorem ipsum dolor sit amet, consectetur adipiscing elit, sed do eiusmod tempor incididunt ut labore et dolore magna aliqua. Ut enim ad minim veniam, quis nostrud exercitation ullamco laboris nisi ut aliquip ex ea commodo consequat Duis aute irure dolor in reprehenderit in voluptate velit esse cillum dolore eu fugiat nulla pariatur. Excepteur, sint occaecat cupidatat non proident, sunt in culpa qui officia deserunt mollit anim id es laborum.</p>
  <span class="read-more">Read more</span>
</article>
<article class="abs blog-card" style="left:650px;top:2398px">
  <div class="photo" style="background:linear-gradient(180deg,#ec8c98,#d9737f 60%,#c9913e)" role="img" aria-label="Woman at a table full of cakes and desserts"></div>
  <p>Lorem ipsum dolor sit amet, consectetur adipiscing elit, sed do eiusmod tempor incididunt ut labore et dolore magna aliqua. Ut enim ad minim veniam, quis nostrud exercitation ullamco laboris nisi ut aliquip ex ea commodo consequat Duis aute irure dolor in reprehenderit in voluptate velit esse cillum dolore eu fugiat nulla pariatur. Excepteur, sint occaecat cupidatat non proident, sunt in culpa qui officia deserunt mollit anim id es laborum.</p>
  <span class="read-more">Read more</span>
</article>

<!-- testimonials -->
<div class="abs testimonials" style="background:linear-gradient(135deg,#e8cdb6,#f1e6dc 45%,#dcc7b5 70%,#cfd0b4)" role="img" aria-label="Hands sketching with a pencil backdrop"></div>
<h2 class="abs serif t-title">Testimonials</h2>
<div class="abs t-card" style="left:59px">
  <div class="avatar" style="background:linear-gradient(180deg,#8a5a3b,#c79a7c)" role="img" aria-label="Reviewer portrait"></div>
  <span class="quote">&ldquo;</span>
  <h4>MARLA T.</h4>
  <p>Lorem ipsum dolor sit amet, consectetur adipiscing elit, sed do eiusmod tempor incididunt ut labore et dolore magna aliqua. Ut enim ad minim veniam, quis nostrud exercitation ullamco laboris nisi ut aliquip ex ea commodo consequat Duis aute irure dolor in reprehenderit in voluptate velit esse cillum dolore eu fugiat nulla pariatur. Excepteur, sint occaecat cupidatat non proident, sunt in culpa qui officia deserunt mollit anim id es laborum.</p>
  <div class="stars"><svg width="42" height="42"><use href="#star"/></svg><svg width="42" height="42"><use href="#star"/></svg><svg width="42" height="42"><use href="#star"/></svg><svg width="42" height="42"><use href="#star"/></svg><svg width="42" height="42"><use href="#star"/></svg></div>
</div>
<div class="abs t-card" style="left:616px">
  <div class="avatar" style="background:linear-gradient(180deg,#4e4640,#d8b49a)" role="img" aria-label="Reviewer portrait"></div>
  <span class="quote">&ldquo;</span>
  <h4>DELAN</h4>
  <p>Lorem ipsum dolor sit amet, consectetur adipiscing elit, sed do eiusmod tempor incididunt ut labore et dolore magna aliqua. Ut enim ad minim veniam, quis nostrud exercitation ullamco laboris nisi ut aliquip ex ea commodo consequat Duis aute irure dolor in reprehenderit in voluptate velit esse cillum dolore eu fugiat nulla pariatur. Excepteur, sint occaecat cupidatat non proident, sunt in culpa qui officia deserunt mollit anim id es laborum.</p>
  <div class="stars"><svg width="42" height="42"><use href="#star"/></svg><svg width="42" height="42"><use href="#star"/></svg><svg width="42" height="42"><use href="#star"/></svg><svg width="42" height="42"><use href="#star"/></svg><svg width="42" height="42"><use href="#star"/></svg></div>
</div>
<svg class="abs" style="left:530px;top:3538px" width="140" height="36" viewBox="0 0 140 36">
  <g fill="none" stroke="#ffffff" stroke-width="3" stroke-linecap="round" stroke-linejoin="round">
    <path d="M52,18 H6 M18,6 L6,18 L18,30"/>
    <path d="M88,18 H134 M122,6 L134,18 L122,30"/>
  </g>
</svg>

<!-- thank you -->
<section class="abs thanks"></section>
<div class="abs" style="left:0;top:3640px;width:675px;height:765px;background:linear-gradient(180deg,#f0b0bc,#d9b6a8 35%,#f4f1ee 60%,#4d6a93 92%)" role="img" aria-label="Two women in white t-shirts with arms crossed"></div>
<h2 class="abs serif thanks-title">THANK YOU !</h2>
<p class="abs thanks-sub">One of our agen will contact you<br>shortly to give you more information</p>
<div class="abs follow">FOLLOW TO<br>UPDATES</div>
<div class="abs news-label">SIGN UP FOR NEWSLETTER</div>
<div class="abs email">YOUR EMAIL</div>
<div class="abs signup">SIGN UP</div>

<!-- footer -->
<footer class="abs footer"></footer>
<div class="abs f-word">The Tavery Parlour</div>
<svg class="abs" style="left:142px;top:4535px" width="40" height="40" viewBox="0 0 40 40"><circle cx="20" cy="20" r="18" fill="none" stroke="#fff" stroke-width="2"/><rect x="10" y="13" width="20" height="14" fill="none" stroke="#fff" stroke-width="2"/><path d="M10,13 L20,21 L30,13" fill="none" stroke="#fff" stroke-width="2"/></svg>
<div class="abs f-icon" style="left:189px;background:#e0221c;border-color:#e0221c" role="img" aria-label="Video channel link"></div>
<svg class="abs" style="left:232px;top:4535px" width="40" height="40" viewBox="0 0 40 40"><path d="M20,34 C12,24 11,20 11,16 A9,9 0 0 1 29,16 C29,20 28,24 20,34 Z" fill="#fff"/><circle cx="20" cy="16" r="3.5" fill="#1d1517"/></svg>
<svg class="abs" style="left:278px;top:4535px" width="40" height="40" viewBox="0 0 40 40"><circle cx="20" cy="20" r="18" fill="none" stroke="#fff" stroke-width="2"/><path d="M13,11 L17,11 L19,16 L16.5,18 C18,21 19.5,22.5 22,24 L24,21.5 L29,23.5 L29,27 C22,28 12,18 13,11 Z" fill="#fff"/></svg>

<div class="abs f-col" style="left:483px;top:4432px"><h5>Navigation</h5><ul><li>Home</li><li>Our story</li><li>Our product</li><li>Testimonial</li></ul></div>
<div class="abs f-col" style="left:704px;top:4432px"><h5>Quick Link</h5><ul><li>Contact Us</li><li>FAQs</li><li>Blog</li><li>Gallery</li><li>Pricing</li></ul></div>
<div class="abs f-col" style="left:911px;top:4434px;width:270px"><h5>Work Hours</h5><p>Monday-Saturday xx am-xx pm</p><p>Lorem ipsum dolor sit amet, consectetur adipiscing elit, sed do eiusmod tempor incididunt ut labore et dolore magna aliqua.</p><span class="call">Call us</span></div>
<div class="abs copy">Copyright &nbsp;2025 The Tavery Parlour. All rights reserved.</div>

</body>
</html>
```